Gluten cove - cover photos - facebooks groups

I have a logo - gluten cove. I have 2 groups that I need cover photos for with the new brand.

Gluten Cove - All Inclusive Reviews

Gluten Cove - Travel Deals

Two separate groups *powered by Getaway Crew* at the bottom of the travel deals in fine print. Not the all inclusive group - that’s powered by 2 agencies - at the bottom powered by 2 celiac travel agents.

I want to keep with the current theme. Maybe the logo, and colour dark block on the left (or whatever standard format to make more going forward) then the versions: deals and all inclusive reviews to the right. Happy, simple, clean. Not cheesy. Match the brand and logo to the group.

Attached are the two current cover photos. (To peach!!) I want the pictures and brand to align with the logo. Happy beach - all inclusive. And international travel and fancy cruise for the travel deals.

I’d like a corporate look that we can scale with any new launch.

Thanks!

```html
<!DOCTYPE html>
<html lang="en">
<head>
<meta charset="utf-8">
<title>Gluten Cove – All Inclusive Reviews cover</title>
<link href="https://fonts.googleapis.com/css2?family=Anton&family=Montserrat:wght@500;600&display=swap" rel="stylesheet">
<style>
  :root{
    --paper:#f4efe9;
    --arch:#efe3d8;
    --navy:#15263b;
    --frame:#6e7884;
    --stripe:#c9ccd0;
    --sun-top:#6f8fae;
    --sun-mid:#e9a24a;
    --sun-low:#b8702e;
    --leaf:#e6ddd2;
  }
  html,body{margin:0;padding:0;overflow:hidden;}
  body{width:1200px;height:676px;background:var(--paper);}
  .cover{position:relative;width:1200px;height:676px;overflow:hidden;
    background:radial-gradient(ellipse at 50% 40%,#f8f4ef 0%,var(--paper) 70%);
    font-family:"Montserrat",Arial,sans-serif;}
  .leaf{position:absolute;background:radial-gradient(ellipse at center,var(--leaf) 0%,rgba(230,221,210,0) 70%);}
  .leaf--tl{left:-40px;top:-40px;width:300px;height:240px;}
  .leaf--tr{right:-40px;top:-30px;width:240px;height:200px;}
  .leaf--br{right:-30px;bottom:-40px;width:300px;height:260px;}
  .frame{position:absolute;left:35px;top:33px;width:1128px;height:609px;border:2px solid var(--frame);box-sizing:border-box;}
  .arch{position:absolute;left:322px;top:91px;width:556px;height:556px;border-radius:50%;background:var(--arch);}
  .stripes{position:absolute;top:426px;}
  .stripes--left{left:37px;width:340px;}
  .stripes--right{left:826px;width:338px;}
  .stripes span{display:block;height:15px;background:var(--stripe);margin-bottom:16px;}
  .brand-badge{position:absolute;left:554px;top:49px;width:92px;height:92px;border-radius:50%;background:var(--navy);
    display:flex;align-items:center;justify-content:center;}
  .brand-badge span{color:#fff;font-family:"Montserrat",Arial,sans-serif;font-weight:600;font-size:12px;letter-spacing:1px;text-align:center;line-height:1.2;}
  .title{position:absolute;left:0;width:1200px;top:178px;margin:0;text-align:center;
    font-family:"Anton",Impact,sans-serif;font-weight:400;line-height:0.86;font-size:200px;letter-spacing:2px;
    background:linear-gradient(180deg,var(--sun-top) 0%,var(--sun-mid) 30%,#d98e3c 48%,#3d5d74 55%,var(--sun-mid) 70%,var(--sun-low) 100%);
    -webkit-background-clip:text;background-clip:text;color:transparent;}
  .title .line{display:block;}
  .title .line--two{margin-top:14px;}
  .subtitle{position:absolute;left:0;width:1200px;top:570px;margin:0;text-align:center;
    font-weight:500;font-size:25px;color:var(--navy);}
  .figure{position:absolute;}
  .figure--hat{left:59px;top:318px;width:285px;height:358px;border-radius:140px 140px 0 0;
    background:linear-gradient(180deg,#1f3a6b 0%,#f0c7a6 45%,#1f3a6b 75%);opacity:.85;}
  .figure--swimmer{left:886px;top:168px;width:256px;height:367px;border-radius:120px 120px 40px 40px;
    background:linear-gradient(180deg,#d84a3c 0%,#b98565 25%,#ffffff 45%,#e05a50 60%,#b98565 100%);opacity:.55;}
</style>
</head>
<body>
<div class="cover">
  <div class="leaf leaf--tl" role="img" aria-label="Faint palm leaf decoration"></div>
  <div class="leaf leaf--tr" role="img" aria-label="Faint palm leaf decoration"></div>
  <div class="leaf leaf--br" role="img" aria-label="Faint palm leaf decoration"></div>

  <div class="frame"></div>
  <div class="arch"></div>

  <div class="stripes stripes--left"><span></span><span></span><span></span><span></span></div>
  <div class="stripes stripes--right"><span></span><span></span><span></span><span></span></div>

  <div class="brand-badge"><span>GLUTEN<br>COVE</span></div>

  <h1 class="title" aria-label="Gluten Cove">
    <span class="line">GLUTEN</span>
    <span class="line line--two">COVE</span>
  </h1>

  <p class="subtitle">- All Inclusive Reviews</p>

  <div class="figure figure--hat" role="img" aria-label="Illustration of a woman in a navy dress holding a wide-brimmed navy sun hat"></div>
  <div class="figure figure--swimmer" role="img" aria-label="Illustration of a vintage bather in a red-and-white striped swimsuit and red cap"></div>
</div>
</body>
</html>
```